Bright-loop designs Business Card

embroidery printing

Target Market(s)

Businesses and public

Industry/Entity Type

Business

Contact Information for Business Card

Front of card..... Bright-loop designs .... Corin Maltby..... 868 512-7361.... Email... bright_loopdesigns@mailbrook.net

Back of card..... Bright-loop designs embroidery & artwork

Colors
000000

```html
<!DOCTYPE html>
<html lang="en">
<head>
<meta charset="utf-8">
<title>Bright-loop designs Business Card</title>
<link rel="stylesheet" href="https://fonts.googleapis.com/css2?family=Source+Sans+3:wght@400;600;700&display=swap">
<style>
  :root {
    --page: #8f8f8f;
    --card-white: #e9e9eb;
    --card-black: #020202;
    --ink: #2b2b2b;
    --ink-soft: #4a4a4a;
    --accent-red: #7a0c04;
    --muted: #2a2a2a;
    --social: #5a5a5a;
  }
  * { margin: 0; padding: 0; box-sizing: border-box; }
  html, body { width: 1105px; height: 1200px; overflow: hidden; }
  body {
    background: var(--page);
    font-family: "Source Sans 3", "Myriad Pro", sans-serif;
    position: relative;
  }
  .card {
    position: absolute;
    left: 180px;
    width: 746px;
    height: 427px;
    overflow: hidden;
  }
  .card-front { top: 110px; background: var(--card-white); }
  .card-back { top: 637px; background: var(--card-black); }

  .brand-name {
    font-weight: 700;
    font-size: 40px;
    letter-spacing: 0.5px;
    white-space: nowrap;
  }
  .card-front .brand-name {
    position: absolute;
    right: 40px;
    top: 68px;
    color: var(--ink);
  }

  .holder { position: absolute; left: 40px; top: 205px; }
  .holder-name { font-size: 27px; font-weight: 600; color: var(--accent-red); line-height: 1.2; }
  .holder-role { font-size: 20px; color: var(--ink); line-height: 1.3; }

  .contacts { position: absolute; left: 40px; top: 283px; list-style: none; }
  .contacts li {
    display: flex; align-items: center; gap: 10px;
    font-size: 19px; color: var(--ink-soft); height: 29px;
  }
  .contacts svg { width: 17px; height: 17px; fill: var(--accent-red); flex: none; }

  .front-band { position: absolute; left: 0; bottom: 0; width: 746px; height: 29px; }

  .card-back .brand-name {
    position: absolute;
    left: 0; right: 0;
    top: 172px;
    text-align: center;
    color: #f2f2f2;
    font-size: 46px;
  }
  .social-row {
    position: absolute;
    left: 0; right: 0; top: 325px;
    display: flex; justify-content: center; align-items: center; gap: 7px;
  }
  .social-row .rule { width: 75px; height: 1px; background: #3a3a3a; }
  .social-dot { width: 30px; height: 30px; border-radius: 50%; background: var(--social); }
  .back-tagline {
    position: absolute; left: 0; right: 0; top: 365px;
    text-align: center; font-size: 13px; color: var(--muted); letter-spacing: 0.5px;
  }
</style>
</head>
<body>
  <section class="card card-front" aria-label="Business card front">
    <div class="brand-name">Bright-loop designs</div>

    <div class="holder">
      <div class="holder-name">Corin Maltby</div>
      <div class="holder-role">CEO/Founder</div>
    </div>

    <ul class="contacts">
      <li>
        <svg viewBox="0 0 24 24" aria-hidden="true"><path d="M6.6 10.8a15.1 15.1 0 0 0 6.6 6.6l2.2-2.2a1 1 0 0 1 1-.25 11.4 11.4 0 0 0 3.6.57 1 1 0 0 1 1 1V20a1 1 0 0 1-1 1A17 17 0 0 1 3 4a1 1 0 0 1 1-1h3.5a1 1 0 0 1 1 1c0 1.25.2 2.45.57 3.6a1 1 0 0 1-.25 1z"/></svg>
        868 512-7361
      </li>
      <li>
        <svg viewBox="0 0 24 24" aria-hidden="true"><path d="M2 5h20v14H2zm2 2v.5l8 5 8-5V7l-8 5z"/></svg>
        bright_loopdesigns@mailbrook.net
      </li>
      <li>
        <svg viewBox="0 0 24 24" aria-hidden="true"><circle cx="12" cy="12" r="10"/></svg>
        www.brightloopdesigns.net
      </li>
    </ul>

    <svg class="front-band" viewBox="0 0 746 29" aria-hidden="true">
      <polygon points="0,0 482,0 474,29 0,29" fill="#050505"/>
      <polygon points="490,0 746,0 746,29 482,29" fill="#7a0c04"/>
    </svg>
  </section>

  <section class="card card-back" aria-label="Business card back">
    <div class="brand-name">Bright-loop designs</div>
    <div class="social-row" aria-label="Social links">
      <span class="rule"></span>
      <span class="social-dot"></span>
      <span class="social-dot"></span>
      <span class="social-dot"></span>
      <span class="social-dot"></span>
      <span class="rule"></span>
    </div>
    <div class="back-tagline">embroidery &amp; artwork for businesses and public</div>
  </section>
</body>
</html>
```